Redesign our updated cannabis seeds website

We are updating our website. Our current website is www.moorkernels.nl or new website is www.kroonvelden.info.

We need an updated design for:
-home page (www.kroonvelden.info) everything between the menu and the footer can be changed. The text we want to keep the same. Suggestions for adding content to the homepage top 5 THC strains, top 5 High Yield, Best Outdoor Cannabis Strains, Best Selling Strains.
-product pages Female Seeds (https://kroonvelden.info/product-category/female-seeds/), Regular Seeds (https://kroonvelden.info/product-category/regular-seeds/) , Autoflower Seeds(https://kroonvelden.info/product-category/autoflowering-seeds/). Everything between the header and the footer can be changed.
-the shop page https://kroonvelden.info/shop/ everything between the main menu and the footer.
-FAQ page https://kroonvelden.info/faqs/ everything between the main menu and the footer.
-Contact page https://kroonvelden.info/contact/ everything between the main menu and the footer.
-Terms and conditions, Shipment Policy, Return Policy, Disclaimer, Cookie Policy, Intellectual Property Claims pages everything between the main menu and the footer.
-All options under my account.

You can login as a customer as:
webteam@moorkern.nl
Kq7&Tz2m!Rw9#Lp4Xc8@Vb3N

Colors to us:
dark green=004820
light green=C7DC67
black= 222 
white= FFFFFF
orange=ff7a04
font color= #222

Preferred fonts:
Header font: Francois One
Body font: Lato

We prefer the artwork files as vector files if possible.

Attached samples of how our packaging looks.
Also under this link www.moorkernels.nl/promokit you can find more images. If any other images are missing that you need please let us know.

Europe

cannabis seeds

5+ page

00AB8E
00BBA5
67D7C9
C6EFE9
E9F9F6
59FF00
82FF00
B8FF75
E3FFCB
F4FFEA

• House colors.

```html
<!DOCTYPE html>
<html lang="en">
<head>
<meta charset="utf-8">
<title>FAQs – Moorkernels seeds</title>
<link href="https://fonts.googleapis.com/css2?family=Francois+One&family=Lato:wght@400;700&display=swap" rel="stylesheet">
<style>
:root{
  --dark-green:#004820;
  --light-green:#C7DC67;
  --ink:#222222;
  --white:#FFFFFF;
  --orange:#ff7a04;
  --panel:#f7f7f7;
  --muted:#555555;
}
*{box-sizing:border-box;margin:0;padding:0}
html,body{width:1200px;height:2933px;overflow:hidden}
body{font-family:'Lato',sans-serif;color:var(--ink);background:var(--white);position:relative}
.abs{position:absolute}
.head{font-family:'Francois One',sans-serif}

/* header */
.site-header{position:absolute;left:0;top:0;width:1200px;height:114px;background:var(--white)}
.brand{left:83px;top:18px;display:flex;align-items:center;gap:10px}
.brand-dot{width:44px;height:44px;border-radius:50%;background:var(--orange)}
.brand-name{font-family:'Francois One',sans-serif;font-size:28px;color:var(--dark-green)}
.top-links{right:83px;top:9px;display:flex;align-items:center;gap:12px;font-size:10px}
.search{width:107px;height:25px;border:1px solid #bbb;border-radius:2px;font-size:10px;color:#aaa;padding:6px 10px;display:flex;justify-content:space-between;align-items:center}
.cart{display:flex;align-items:center;gap:3px}
.flags{display:flex;gap:8px}
.flag{width:12px;height:8px}
.main-nav{right:83px;top:62px;display:flex;gap:32px;font-size:10px;text-transform:uppercase;color:#444}
.main-nav .active{color:var(--dark-green);font-weight:700}

/* hero */
.hero{left:0;top:114px;width:1200px;height:290px;background:radial-gradient(ellipse at 45% 50%,#4c7f2e 0%,#2a5a1e 45%,#163a12 100%)}
.hero h1{position:absolute;left:83px;top:92px;font-family:'Francois One',sans-serif;font-weight:400;color:var(--white);font-size:40px}

/* faq */
.faq-open{left:83px;width:1034px;height:137px;background:var(--panel);padding:26px 18px}
.faq-open h3{font-weight:400;font-size:20px;margin-bottom:24px}
.faq-open p{font-size:13px;line-height:20px;color:var(--muted)}
.faq-open .sign{position:absolute;right:22px;top:40px;width:20px;height:2px;background:var(--ink)}
.faq-bar{left:83px;width:1034px;height:64px;background:var(--light-green);font-family:'Francois One',sans-serif;font-size:20px;display:flex;align-items:center;justify-content:space-between;padding:0 24px 0 18px}
.plus{width:20px;height:20px;position:relative}
.plus::before,.plus::after{content:"";position:absolute;background:var(--ink)}
.plus::before{left:0;top:9px;width:20px;height:2.5px}
.plus::after{left:9px;top:0;width:2.5px;height:20px}
.group-title{left:83px;font-family:'Francois One',sans-serif;font-size:32px;font-weight:400}

/* contact band */
.contact-band{left:0;top:1877px;width:1200px;height:566px;background:var(--dark-green);color:var(--white)}
.contact-band h2{position:absolute;top:24px;width:100%;text-align:center;font-size:21px;font-weight:700}
.contact-band .lead{position:absolute;top:75px;width:100%;text-align:center;font-size:13px;line-height:21px}
.field{position:absolute;left:171px;width:858px;height:52px;background:var(--white);color:#999;font-size:13px;padding:18px 18px}
.submit{position:absolute;left:521px;top:488px;width:158px;height:46px;background:var(--orange);font-family:'Francois One',sans-serif;font-size:17px;display:flex;align-items:center;justify-content:center}

/* footer */
.site-footer{left:0;top:2443px;width:1200px;height:407px;background:var(--panel)}
.col{position:absolute;top:48px;font-size:13px;color:#666}
.col h4{font-family:'Francois One',sans-serif;font-weight:400;font-size:17px;color:var(--ink);margin-bottom:10px}
.col li{list-style:none;height:32px}
.contact-line{display:flex;gap:10px;align-items:flex-start}
.socials{position:absolute;left:905px;top:297px;display:flex;gap:10px}
.social{width:20px;height:20px;border-radius:50%;background:var(--orange)}
.cards{position:absolute;left:88px;top:320px;display:flex;gap:36px}
.card{width:96px;height:44px;border-radius:6px;font-weight:700;font-size:17px;display:flex;align-items:center;justify-content:center}
.copyright{left:0;top:2850px;width:1200px;height:83px;background:var(--dark-green);color:var(--white);font-size:13px;font-weight:700;display:flex;align-items:center;justify-content:center}
</style>
</head>
<body>

<header class="site-header">
  <div class="abs brand"><span class="brand-dot"></span><span class="brand-name">Moorkernels</span></div>
  <div class="abs top-links">
    <span>Cart</span><span>Shop</span><span>FAQs</span><span>Contacts</span>
    <span class="search">Search
      <svg width="11" height="11" viewBox="0 0 11 11"><circle cx="4.5" cy="4.5" r="3.5" fill="none" stroke="#999" stroke-width="1.3"/><line x1="7" y1="7" x2="10" y2="10" stroke="#999" stroke-width="1.3"/></svg>
    </span>
    <span class="cart"><svg width="13" height="11" viewBox="0 0 13 11"><path d="M0 1h2l2 6h7l1.5-5H3" fill="none" stroke="#7ab51d" stroke-width="1.4"/><circle cx="5" cy="9.5" r="1.2" fill="#7ab51d"/><circle cx="10" cy="9.5" r="1.2" fill="#7ab51d"/></svg>0 Items</span>
    <span class="flags"><span class="flag" style="background:#e8b01c"></span><span class="flag" style="background:#3a55a4"></span><span class="flag" style="background:#c8102e"></span></span>
  </div>
  <nav class="abs main-nav">
    <span class="active">Cannabis Seeds Videos ⌄</span>
    <span>Female Seeds ⌄</span>
    <span>Regular Seeds ⌄</span>
    <span>Autoflowering Seeds ⌄</span>
    <span>Blogs ⌄</span>
  </nav>
</header>

<section class="abs hero" role="img" aria-label="Close-up photo of green cannabis leaves">
  <h1>FAQs</h1>
</section>

<div class="abs faq-open" style="top:437px">
  <h3>What will my package look like?</h3>
  <span class="sign"></span>
  <p>Your order will be packed in a discrete padded envelope or a small cardboard box that will fit in your mailbox. The package will also have a discrete shipper as return address.</p>
</div>
<div class="abs faq-bar" style="top:597px">How many seeds does 1 package contain?<span class="plus"></span></div>
<div class="abs faq-bar" style="top:676px">How long my order will take to arrive?<span class="plus"></span></div>
<div class="abs faq-bar" style="top:755px">How is your order shipped?<span class="plus"></span></div>
<div class="abs faq-bar" style="top:834px">How do i order?<span class="plus"></span></div>
<div class="abs faq-bar" style="top:915px">Can I order from my country?<span class="plus"></span></div>

<h2 class="abs group-title" style="top:1030px">Payment Questions:</h2>
<div class="abs faq-bar" style="top:1087px">Payment options?<span class="plus"></span></div>

<h2 class="abs group-title" style="top:1204px">Product Questions:</h2>
<div class="abs faq-open" style="top:1261px">
  <h3>Why do sativa strains take longer to flower?</h3>
  <span class="sign"></span>
  <p>Sativa strains are naturally found in parts of the world with hot sunny climates. Original landrace Sativa strains can take from 12-16 weeks to flower and fully ripen. Many modern day Sativa strains are shorter in flowering time to suit commercial value, yet the grower can still expect the original haze traits.</p>
</div>
<div class="abs faq-bar" style="top:1422px">What strains are suitable for beginners?<span class="plus"></span></div>
<div class="abs faq-bar" style="top:1503px">Which sativa strains are tastiest?<span class="plus"></span></div>
<div class="abs faq-bar" style="top:1581px">Very tasty indica strains?<span class="plus"></span></div>
<div class="abs faq-bar" style="top:1661px">Can I grow seeds legally? If not can I still buy them?<span class="plus"></span></div>
<div class="abs faq-bar" style="top:1742px">Biggest yielding sativa strains?<span class="plus"></span></div>

<section class="abs contact-band">
  <h2>Do you have any questions?</h2>
  <p class="lead">Thank you for using Moorkernels SEEDS! Please complete this form, So we can provide<br>Quick and Efficient Service! If you have urgent</p>
  <div class="field" style="top:139px">Name</div>
  <div class="field" style="top:204px">Email</div>
  <div class="field" style="top:270px">Phone No.</div>
  <div class="field" style="top:337px;height:118px">Message</div>
  <div class="submit">Submit</div>
</section>

<footer class="abs site-footer">
  <div class="col" style="left:83px">
    <h4>Categories</h4>
    <ul><li>Autoflowering Cannabis Seeds</li><li>Buy Cannabis Seeds</li><li>Cannabis Aroma Flavor And Medicinal Benefits</li><li>Cannabis Seeds</li><li>Cannabis Aroma Flavor And Medicinal Benefits</li></ul>
  </div>
  <div class="col" style="left:471px">
    <h4>My Account</h4>
    <ul><li>Checkout</li><li>My Account</li><li>Shop</li><li>Orders</li><li>Account details</li><li>Lost password</li></ul>
  </div>
  <div class="col" style="left:666px">
    <h4>Quick Links</h4>
    <ul><li>Shop</li><li>FAQs</li><li>Contact us</li><li>Terms &amp; Conditions</li><li>Shipment Policy</li><li>Return Policy</li><li>Disclaimer</li><li>Cookie Policy</li><li>Intellectual Property Claims</li></ul>
  </div>
  <div class="col" style="left:905px">
    <h4>Contact Info</h4>
    <ul>
      <li class="contact-line"><svg width="16" height="12" viewBox="0 0 16 12"><rect x="1" y="1" width="14" height="10" fill="none" stroke="#4caf50" stroke-width="1.3"/><path d="M1 1l7 6 7-6" fill="none" stroke="#4caf50" stroke-width="1.3"/></svg>info@moorkernels.nl</li>
      <li class="contact-line"><svg width="16" height="14" viewBox="0 0 16 16"><path d="M3 1l3 3-2 2c1 2 3 4 5 5l2-2 3 3-2 3C7 15 1 9 1 3z" fill="none" stroke="#4caf50" stroke-width="1.3"/></svg>+31 (0)20 – 555 0147</li>
      <li class="contact-line" style="height:auto"><svg width="16" height="18" viewBox="0 0 16 18"><path d="M8 17s6-6 6-10A6 6 0 0 0 2 7c0 4 6 10 6 10z" fill="none" stroke="#4caf50" stroke-width="1.3"/><circle cx="8" cy="7" r="2" fill="none" stroke="#4caf50" stroke-width="1.3"/></svg><span>Kadelaan 14 1046XR<br>Amsterdam Nederland</span></li>
    </ul>
  </div>
  <div class="col" style="left:905px;top:265px"><h4>Follow Us Social Media</h4></div>
  <div class="socials"><span class="social"></span><span class="social"></span><span class="social"></span></div>
  <div class="cards">
    <span class="card" style="color:#1a4fa0">CardPay</span>
    <span class="card" style="background:#e8322a;color:#fff;width:72px;font-size:14px">NetCard</span>
  </div>
</footer>

<div class="abs copyright">Copyright&nbsp; © 2022 Moorkernels seeds</div>

</body>
</html>
```